Packaging Design Project

I need a box for a hair oil called NEL. 3 color, Simple design .. We are open to new ideas, the over all theme.. Pure and Simple , Natural, Color protect, good for the hair. We started with a basic design and this is the existing website http://nelhaircare.com/

Industry/Entity Type

Hair

```html
<!DOCTYPE html>
<html lang="en">
<head>
<meta charset="utf-8">
<title>NEL Protective Hair Oil – Box Dieline</title>
<link rel="stylesheet" href="https://fonts.googleapis.com/css2?family=Arimo:ital,wght@0,400;0,700;1,400&display=swap">
<style>
  :root {
    --brand-red: #c5402b;
    --paper: #ffffff;
    --canvas-bg: #ffffff;
    --cut-line: #c9c9c9;
    --fold-line: #dedede;
    --text-grey: #6f6f6f;
    --photo-dark: #5a2a24;
    --photo-mid: #9a625b;
    --photo-light: #f1ebe8;
  }
  * { box-sizing: border-box; margin: 0; padding: 0; }
  html, body { width: 1200px; height: 900px; overflow: hidden; background: var(--canvas-bg); }
  body { font-family: "Arimo", Arial, sans-serif; }
  .canvas { position: relative; width: 1200px; height: 900px; overflow: hidden; }
  .dieline { position: absolute; inset: 0; }
  .panel-text { position: absolute; inset: 0; }

  .brand-name {
    position: absolute; color: var(--brand-red); font-weight: 400;
    font-size: 40px; letter-spacing: 2px; text-align: center; line-height: 1;
  }
  .product-title {
    position: absolute; color: var(--brand-red); text-align: center; line-height: 1.15;
    font-weight: 400; white-space: nowrap;
  }
  .product-title .name { display: block; font-weight: 700; font-size: 12.5px; }
  .product-title .sub { display: block; font-weight: 400; font-size: 9px; }

  .back-panel .brand-name { left: 92px; width: 182px; top: 262px; }
  .back-panel .product-title { left: 92px; width: 182px; top: 324px; }
  .directions {
    position: absolute; left: 113px; top: 361px; white-space: nowrap;
    font-style: italic; font-size: 11px; color: var(--text-grey);
  }

  .front-panel .photo {
    position: absolute; left: 377px; top: 224px; width: 180px; height: 232px;
    background:
      linear-gradient(180deg, transparent 60%, var(--paper) 100%),
      linear-gradient(100deg, var(--photo-light) 0%, var(--photo-light) 30%, var(--photo-mid) 55%, var(--photo-dark) 80%, var(--photo-mid) 100%);
  }
  .front-panel .brand-name { left: 376px; width: 181px; top: 437px; }
  .front-panel .product-title { left: 376px; width: 181px; top: 510px; }
  .front-panel .product-title .name { font-size: 13px; }
  .tagline {
    position: absolute; left: 376px; width: 181px; top: 560px; text-align: center; white-space: nowrap;
    font-style: italic; font-size: 11px; line-height: 1.3; color: var(--text-grey);
  }
  .tagline em { color: var(--brand-red); }
  .claims, .volume {
    position: absolute; top: 633px; font-size: 8px; line-height: 1.35;
    color: var(--paper); white-space: nowrap;
  }
  .claims { left: 393px; }
  .volume { left: 522px; }

  .side-panel {
    position: absolute; left: 570px; top: 240px; width: 84px; white-space: nowrap;
    font-style: italic; font-size: 6.5px; line-height: 1.35; color: var(--text-grey);
  }
  .side-panel .more-info { margin-top: 12px; color: var(--brand-red); }
</style>
</head>
<body>
<main class="canvas">
  <svg class="dieline" width="1200" height="900" viewBox="0 0 1200 900" aria-hidden="true">
    <path d="M92 222 L40 232 V662 L92 672 Z" fill="var(--paper)" stroke="var(--cut-line)"/>
    <path d="M376 218 V145 L383 140 V90 Q383 62 410 60 H523 Q550 62 550 90 V140 L557 145 V218 Z" fill="var(--brand-red)"/>
    <line x1="383" y1="140" x2="550" y2="140" stroke="var(--paper)" stroke-width="0.8"/>
    <path d="M274 218 V165 L290 145 H362 L376 160 V218 Z" fill="var(--brand-red)"/>
    <path d="M557 218 V160 L571 145 H645 L660 165 V218 Z" fill="var(--brand-red)"/>
    <path d="M376 678 V745 L383 752 V805 Q383 833 410 835 H523 Q550 833 550 805 V752 L557 745 V678 Z" fill="var(--brand-red)"/>
    <line x1="383" y1="752" x2="550" y2="752" stroke="var(--paper)" stroke-width="0.8"/>
    <path d="M274 678 V730 L290 752 H362 L376 735 V678 Z" fill="var(--brand-red)"/>
    <path d="M557 678 V735 L571 752 H645 L660 730 V678 Z" fill="var(--brand-red)"/>
    <path d="M150 678 V710 Q150 718 158 718 H207 Q215 718 215 710 V678 Z" fill="var(--brand-red)"/>
    <rect x="92" y="218" width="568" height="460" fill="var(--paper)" stroke="var(--cut-line)"/>
    <rect x="92" y="622" width="568" height="56" fill="var(--brand-red)"/>
    <g stroke="var(--fold-line)" stroke-width="1">
      <line x1="274" y1="224" x2="274" y2="622"/>
      <line x1="376" y1="224" x2="376" y2="622"/>
      <line x1="557" y1="224" x2="557" y2="622"/>
      <line x1="660" y1="224" x2="660" y2="622"/>
    </g>
    <g class="icons" fill="none" stroke="var(--brand-red)" stroke-width="1.6">
      <circle cx="322" cy="263" r="13" fill="var(--brand-red)" stroke="none"/>
      <path d="M322 330 C311 322 312 312 316 308 C318 314 320 316 322 318 C324 316 326 314 328 308 C332 312 333 322 322 330 Z" fill="var(--brand-red)" stroke="none"/>
      <line x1="322" y1="330" x2="322" y2="340"/>
      <circle cx="322" cy="417" r="16" fill="var(--brand-red)" stroke="none"/>
      <circle cx="322" cy="502" r="16"/>
      <line x1="311" y1="513" x2="333" y2="491"/>
      <path d="M310 590 L316 580 L322 590 M328 572 L334 582 L322 584 M316 574 L328 574"/>
    </g>
  </svg>

  <section class="panel-text back-panel">
    <div class="brand-name">NEL</div>
    <h2 class="product-title"><span class="name">PROTECTIVE HAIR OIL</span><span class="sub">TREATMENT AND STYLING AID</span></h2>
    <p class="directions">Directions for use:</p>
  </section>

  <section class="panel-text front-panel">
    <div class="photo" role="img" aria-label="Photograph of a woman with long glossy auburn hair"></div>
    <div class="brand-name">NEL</div>
    <h1 class="product-title"><span class="name">PROTECTIVE HAIR OIL</span><span class="sub">TREATMENT AND STYLING AID</span></h1>
    <p class="tagline">Style, Smooth, Shine and<br>Condition <em>ALL</em> Hair Types<br>while locking In moisture</p>
    <p class="claims">Paraben Free - Sulfate Free<br>Allergy Tested - Alcohol Free</p>
    <p class="volume">100ml<br>3.4oz</p>
  </section>

  <section class="side-panel">
    <p>Formulated for NEL,<br>Cedar Grove,<br>Oregon</p>
    <p class="more-info">For more information<br>visit us at:<br>www.NELHAIRCARE.com</p>
  </section>
</main>
</body>
</html>
```